Wordpress Website design partner needed for an Arabic Language Institute for English Speakers

We are an online Arabic Language institute, targeting English Speakers around the world and we provide online courses and private group and one on one classes
We are looking for a total of 5 pages designed.
The Design should be mobile-first, and then provide PC for any differences.
I am looking for a consistent design with a lot of white space and in line with our Logo colours.
Images used should be around the theme of Arabic Language/Islamic in Nature, so please do not use any illustrations or images of animals or human beings except for silhouettes or images without faces visible, such as someone facing other way or below torso or hands etc.
The website will eventually be prepared for Wordpress using Divi.
I will provide a very structured outline of what elements and modules each page should have. Therefore I am looking for someone that has an eye for detail and is precise in executing requirements.
I decided to post on this site because I am looking for a long-term partner that can take care of any of our design needs as they come up.
More details to follow
I will do abit more research tomorrow to suggest sample sites
Updates
Target Market(s)
English speakers that want to learn Arabic for Religous purposes such as understanding the Quran
Industry/Entity Type
Education
Colors
Designer to choose colors to be used in the design.
Requirements
Must have
- Mobile First, and design for PC for changes
- Consistency
- Plenty of White Space
- Colour Palette based on Logo
- Colour and Transparent/White Header for when scrolling
- Big Call to Action buttons with contrasting colors
- A consistent footer for all pages with
- -Social Media Icons
- -Contact us
- -Sitemap
- -Copyright
- -Logo
- Anything with a hashtag (#) beforehand in the Doc file means it should be a module like the modules used in Divi Theme, Please check the following website for an explanation of what each module consists of and some examples of it in use. https://www.trelvanoblockshowcase.com/trelvano-blocks-guide/
Nice to have
- Parallax Effect
Should not have
- illustrations or images of animals or human beings except for silhouettes or images without faces visible, such as someone facing other way or below torso or hands etc.

```html
<!DOCTYPE html>
<html lang="en">
<head>
<meta charset="utf-8">
<title>Al-Miftah Arabic Academy</title>
<link rel="stylesheet" href="https://fonts.googleapis.com/css2?family=Roboto:wght@300;400;500;700&display=swap">
<style>
:root{
  --navy:#1c3e92;
  --royal:#1d4f9c;
  --brand-blue:#1a3f94;
  --testimonial:#1d5f9a;
  --teal:#2a93a8;
  --teal-light:#2a8fa8;
  --ink:#1b1b1b;
  --muted:#3a3a3a;
  --panel:#f0f5fc;
  --panel-line:#c3ccd8;
  --white:#ffffff;
}
*{box-sizing:border-box;margin:0;padding:0}
html,body{width:1200px;height:3601px;overflow:hidden}
body{font-family:"Roboto",Arial,sans-serif;color:var(--ink);background:var(--white);position:relative}
section,header,footer{position:absolute;left:0;width:1200px}
.abs{position:absolute}

/* header */
.site-header{top:0;height:104px;background:var(--white)}
.brand{left:140px;top:22px;display:flex;align-items:center;gap:12px}
.brand-mark{width:48px;height:48px;background:var(--teal-light);border-radius:4px}
.brand-name{font-size:22px;font-weight:700;color:var(--royal);letter-spacing:2px;line-height:1}
.main-nav{top:46px;left:545px;display:flex;gap:0}
.main-nav a{position:absolute;font-size:15px;color:#333;text-decoration:none;white-space:nowrap}
.main-nav a.active{color:var(--royal);font-weight:500}

/* intro band */
.intro{top:104px;height:244px;background:linear-gradient(90deg,#1e5aa0 0%,#23719f 60%,#2a8fa8 100%)}
.intro p{left:157px;top:46px;width:700px;color:var(--white);font-size:20.5px;line-height:32px;font-weight:400}
.btn-outline{border:2px solid var(--white);color:var(--white);font-weight:500;font-size:15px;display:flex;align-items:center;justify-content:center;text-decoration:none}
.intro .btn-outline{left:161px;top:162px;width:197px;height:48px;border-radius:2px}
.play{left:927px;top:75px;width:74px;height:74px}

/* hero */
.hero{top:348px;height:577px}
.hero-photo{position:absolute;inset:0;background:linear-gradient(180deg,#5f6b86 0%,#8a8b9c 30%,#c7a88a 52%,#6c6a72 64%,#3d4452 100%)}
.hero-shade{position:absolute;inset:0;background:rgba(0,0,0,.22)}
.hero h1{left:0;width:1200px;top:168px;text-align:center;color:var(--white);font-size:40px;font-weight:700}
.hero .lead{left:260px;width:680px;top:224px;text-align:center;color:var(--white);font-size:21.5px;line-height:28px}
.hero .btn-outline{left:507px;top:310px;width:181px;height:43px;border-radius:2px}
.dots{top:534px;left:558px;display:flex;gap:8px}
.dots span{width:14px;height:14px;border-radius:50%;background:var(--white);border:2px solid var(--white)}
.dots span.off{background:transparent}

/* values */
.values{top:925px;height:433px}
.value{width:300px;text-align:center}
.value svg{display:block;margin:0 auto}
.value h3{margin-top:14px;font-size:23px;font-weight:700;color:var(--royal)}
.value p{margin-top:10px;font-size:13px;line-height:23px;color:var(--muted)}

/* testimonials */
.testimonials{top:1358px;height:368px;background:var(--testimonial);color:var(--white)}
.section-title{width:1200px;left:0;text-align:center;font-size:24px;font-weight:700}
.testimonials .section-title{top:70px}
.quote{width:370px;top:148px;font-size:13.5px;line-height:20px}
.quote strong{display:block;margin-top:6px;font-weight:700;font-size:14.5px}
.arrow{top:180px;width:24px;height:36px}

/* strategies */
.strategies{top:1726px;height:381px}
.strategies h2{left:0;width:1200px;top:88px;text-align:center;font-size:27px;line-height:36px;font-weight:700}
.strategies p{left:230px;width:740px;top:180px;text-align:center;font-size:16px;line-height:23px;color:var(--muted)}
.btn-solid{background:var(--brand-blue);color:var(--white);font-size:16px;font-weight:700;display:flex;align-items:center;justify-content:center;text-decoration:none;border-radius:2px}
.strategies .btn-solid{left:521px;top:254px;width:169px;height:46px}

/* countdown */
.countdown{top:2107px;height:300px;background:var(--teal);color:var(--white)}
.countdown .label-top{left:0;width:1214px;top:55px;text-align:center;font-size:30px;font-weight:300}
.unit{width:160px;text-align:center;top:118px}
.unit .num{font-size:52px;font-weight:300;line-height:60px;letter-spacing:1px}
.unit .cap{font-size:23px;font-weight:300}
.colon{top:126px;font-size:42px;font-weight:300}

/* features accordion */
.features{top:2407px;height:637px}
.features .section-title{top:68px;color:var(--ink);left:6px}
.acc{left:198px;width:788px;height:53px;background:var(--panel);border:1px solid var(--panel-line);display:flex;align-items:center;justify-content:space-between;padding:0 22px 0 30px;font-size:16.5px}
.acc .sign{font-size:20px;color:#333}
.acc.open{background:var(--white);height:177px;align-items:flex-start;flex-direction:column;justify-content:flex-start;padding-top:14px}
.acc.open .row{display:flex;width:100%;justify-content:space-between}
.acc.open p{margin-top:14px;font-size:13px;line-height:27px;color:#555}

/* keep in touch */
.keep{top:3044px;height:430px;background:var(--navy);color:var(--white)}
.keep h2{left:163px;top:108px;font-size:29px;font-weight:700}
.keep p{left:164px;top:152px;width:450px;font-size:14.5px;line-height:27px}
.field{left:686px;width:348px;height:47px;background:var(--white);color:#333;font-size:13px;display:flex;align-items:center;padding-left:21px}
.keep .join{left:686px;top:267px;width:348px;height:50px;border:2px solid var(--white);font-size:16px;font-weight:700;border-radius:3px}

/* footer */
.site-footer{top:3474px;height:127px}
.foot-nav a{position:absolute;top:39px;font-size:15px;color:#333;text-decoration:none}
.copy{left:174px;top:77px;font-size:11.5px;color:#444}
.social{top:32px;left:893px;display:flex;gap:7px}
.social span{width:32px;height:32px;border-radius:50%;display:block}
</style>
</head>
<body>

<header class="site-header">
  <div class="brand abs">
    <span class="brand-mark"></span>
    <span class="brand-name">AL-MIFTAH</span>
  </div>
  <nav class="main-nav abs">
    <a class="active" style="left:0">HOME</a>
    <a style="left:94px">ABOUT US</a>
    <a style="left:215px">CONTACT US</a>
    <a style="left:357px">OUR COURSES</a>
  </nav>
</header>

<section class="intro">
  <p class="abs">The Arabic Language Academy which helps understand Allah’s words and the Noble Prophets teachings directly in the most Effective, Efficient and Effortless way. Never rely on translations again!</p>
  <a class="btn-outline abs">Start Learning Now</a>
  <svg class="play abs" viewBox="0 0 74 74" aria-label="Play video">
    <circle cx="37" cy="37" r="37" fill="#fff"/>
    <path d="M30 24 L50 37 L30 50 Z" fill="#111"/>
  </svg>
</section>

<section class="hero">
  <div class="hero-photo" role="img" aria-label="Photograph of a mosque with minarets reflected in still water at dusk"></div>
  <div class="hero-shade"></div>
  <h1 class="abs">WELCOME TO AL-MIFTAH</h1>
  <p class="lead abs">Aliquam enim Proin dui lectus cursus eu mattis laoreet viverra sit amet quam Curabitur vel dolor ultrices ipsum dictum</p>
  <a class="btn-outline abs">Get Started</a>
  <div class="dots abs"><span class="off"></span><span></span><span></span><span></span></div>
</section>

<section class="values">
  <div class="value abs" style="left:127px;top:97px">
    <svg width="72" height="72" viewBox="0 0 72 72" fill="none" stroke="#1d5f9a" stroke-width="2.5">
      <circle cx="36" cy="36" r="32"/>
      <path d="M36 14 V36 H50" stroke-linecap="round"/>
      <g stroke-width="2"><path d="M36 8v4M36 60v4M8 36h4M60 36h4"/></g>
    </svg>
    <h3>EFFICIENT</h3>
    <p>Nunc tempus felis vitae urna Vivamus porttitor neque at volutpat rutrum purus nisi eleifend libero a tempus libero lectus feugiat felis Morbi</p>
  </div>
  <div class="value abs" style="left:455px;top:97px">
    <svg width="72" height="72" viewBox="0 0 72 72" fill="none" stroke="#1d5f9a" stroke-width="2.5" stroke-linecap="round">
      <path d="M36 14a16 16 0 0 0-9 29v7h18v-7a16 16 0 0 0-9-29z"/>
      <path d="M29 56h14M31 62h10M36 50V34M31 30l5 4 5-4"/>
      <path d="M36 2v6M14 10l4 4M58 10l-4 4M8 30h5M59 30h5"/>
    </svg>
    <h3>EFFECTIVE</h3>
    <p>Nunc tempus felis vitae urna Vivamus porttitor neque at volutpat rutrum purus nisi eleifend libero a tempus libero lectus feugiat felis Morbi</p>
  </div>
  <div class="value abs" style="left:782px;top:97px">
    <svg width="72" height="72" viewBox="0 0 72 72" role="img" aria-label="Icon of hands raised in prayer">
      <rect x="14" y="8" width="44" height="58" rx="22" fill="#d6e6f2"/>
    </svg>
    <h3>EFFORTLESS</h3>
    <p>Nunc tempus felis vitae urna Vivamus porttitor neque at volutpat rutrum purus nisi eleifend libero a tempus libero lectus feugiat felis Morbi</p>
  </div>
</section>

<section class="testimonials">
  <h2 class="section-title abs">TESTIMONIALS</h2>
  <svg class="arrow abs" style="left:98px" viewBox="0 0 24 36"><path d="M18 4 L6 18 L18 32" fill="none" stroke="#8fb3d3" stroke-width="4"/></svg>
  <div class="quote abs" style="left:199px">Aliquam enim Proin dui lectus cursus eu mattis laoreet viverra sit amet quam Curabitur vel dolor ultrices ipsum dictum tristique Praesent vitae lacus Ut velit enim vestibulum non Curabitur iaculis tempus eros<strong>By Author Name</strong></div>
  <div class="quote abs" style="left:655px">Aliquam enim Proin dui lectus cursus eu mattis laoreet viverra sit amet quam Curabitur vel dolor ultrices ipsum dictum tristique Praesent vitae lacus Ut velit enim vestibulum non Curabitur iaculis tempus eros<strong>By Author Name</strong></div>
  <svg class="arrow abs" style="left:1098px" viewBox="0 0 24 36"><path d="M6 4 L18 18 L6 32" fill="none" stroke="#8fb3d3" stroke-width="4"/></svg>
</section>

<section class="strategies">
  <h2 class="abs">7 LEARNING STRATEGIES THAT WILL BOOST<br>YOUR ARABIC LEARNING INSTANTLY</h2>
  <p class="abs">aliquam enim Proin dui lectus cursus eu mattis laoreet viverra sit amet quam Curabitur vel dolor ultrices ipsum dictum tristique Praesent vitae lacus Ut velit enim vestibulu</p>
  <a class="btn-solid abs">Book your spot</a>
</section>

<section class="countdown">
  <div class="label-top abs">Launching In</div>
  <div class="unit abs" style="left:242px"><div class="num">000</div><div class="cap">Days</div></div>
  <div class="colon abs" style="left:402px">:</div>
  <div class="unit abs" style="left:420px"><div class="num">000</div><div class="cap">Hours</div></div>
  <div class="colon abs" style="left:588px">:</div>
  <div class="unit abs" style="left:605px"><div class="num">000</div><div class="cap">Mins</div></div>
  <div class="colon abs" style="left:772px">:</div>
  <div class="unit abs" style="left:792px"><div class="num">000</div><div class="cap">Secs</div></div>
</section>

<section class="features">
  <h2 class="section-title abs">FEATURES</h2>
  <div class="acc abs" style="top:131px"><span>24/7 Access</span><span class="sign">+</span></div>
  <div class="acc abs" style="top:198px"><span>Learn at your own Pace</span><span class="sign">+</span></div>
  <div class="acc abs" style="top:265px"><span>Certificate</span><span class="sign">+</span></div>
  <div class="acc abs" style="top:332px"><span>Free Study Material</span><span class="sign">+</span></div>
  <div class="acc open abs" style="top:399px">
    <div class="row"><span>Qualified Teachers</span><span class="sign">-</span></div>
    <p>Nunc tempus felis vitae urna Vivamus porttitor neque at volutpat rutrum purus nisi eleifend libero a tempus libero lectus feugiat felis Morbi diam mauris viverra in gravida eu mattis in ante Morbi eget arcu Morbi porta libero id ullamcorper nonummy nibh ligula pulvinar metus eget consectetuer augue nisi quis lacus</p>
  </div>
</section>

<section class="keep">
  <h2 class="abs">KEEP IN TOUCH</h2>
  <p class="abs">Nunc tempus felis vitae urna Vivamus porttitor neque at volutpat rutrum purus nisi eleifend libero a tempus libero lectus feugiat felis Morbi diam mauris viverra in gravida eu mattis in ante Morbi eget arcu Morbi porta libero id ullamcorper nonummy nibh ligula pulvinar metus eget</p>
  <div class="field abs" style="top:96px">First Name</div>
  <div class="field abs" style="top:153px">Last Name</div>
  <div class="field abs" style="top:209px">Email</div>
  <a class="btn-outline join abs">JOIN TODAY</a>
</section>

<footer class="site-footer">
  <nav class="foot-nav">
    <a style="left:174px">HOME</a>
    <a style="left:268px">ABOUT US</a>
    <a style="left:390px">CONTACT US</a>
    <a style="left:531px">OUR COURSES</a>
  </nav>
  <div class="copy abs">© 2020 Company Name | All Rights Reserved | Disclaimer</div>
  <div class="social abs">
    <span style="background:#2f4f9a"></span>
    <span style="background:#3f8fd0"></span>
    <span style="background:#2d5f94"></span>
    <span style="background:#1f5fa8"></span>
  </div>
</footer>

</body>
</html>
```